ZB - WESITE NEEDED PAGE: Clean / Modern / Pro & Dynamic

Zephyl-Brokers is a new insurance brokerage firm dealing exclusively with companies (BToB) providing the following property: Liabilities Insurance Insurances Automobile Insurance Insurances Construction% 26amp; Engineering Casualty Workmen 's Compensation Health Insurance Marime% 26amp; Transit Credit Insurance Young, Fast, Proactive and Dynamic we call ourselves Zephyl-Brokers because we are a "start-up" willing to make a difference in the market, bringing modernity and speed to our industry, still too bureaucratic / procedural / opaque uninitiated. We need something respecting the colors of our orange logtype; blue; white; black; easy to scroll, with simple information on the company; - who we are - our team (with the pictures) - what we do - what we do - contact us, contact us (google map) Luanda (Angola) Small company, just need something flashy / professional / structured / modern.

Target Market(s)

BtoB; Oil and gas companies; French speaking copying established in Angola, all industrials, factories and importers of goods.

Industry/Entity Type

Insurance Broker

Font styles to use
Sans Serif

Colors

Requirements
Must have
• We need something respecting the colors of our orange logtype; blue; white; black; easy to scroll, with simple information on the company; - who we are - our team (with the pictures) - what we do - what we do - contact us, contact us (google map) Luanda (Angola) Small company, just need something flashy / professional / structured / modern.
Nice to have
• A page format
Should not have
• WE DO NOT WANT A REFER TO OUR LOGO, but a Home Page for our Website with the basics categories ... >> PLEASE CAREFULLY USE THE RIGHT COLOR OF THE LOGOTYPE which are the ones enclosed Orange / Turquoise / Black as per the business card .

```html
<!DOCTYPE html>
<html lang="en">
<head>
<meta charset="utf-8">
<title>Zephyl-Brokers — Insurance Brokerage</title>
<link href="https://fonts.googleapis.com/css2?family=Poppins:wght@300;400;500;600;700;800&display=swap" rel="stylesheet">
<style>
:root{
  --navy:#1d2a6b;
  --blue:#2f47b5;
  --blue-light:#5b73e0;
  --violet:#6a4fd1;
  --orange:#f7941d;
  --coral:#f2665a;
  --sky:#2e8fe0;
  --teal:#17a894;
  --ink:#1c1c2b;
  --text:#6b6f80;
  --pale:#eef3fb;
  --pale-blue:#d9ecfa;
  --ring:#dcd6f5;
  --white:#ffffff;
  --footer:#23252b;
}
*{box-sizing:border-box;margin:0;padding:0}
html,body{width:1200px;height:2688px;overflow:hidden}
body{font-family:"Poppins",Arial,sans-serif;color:var(--text);background:var(--white);position:relative}
.page{position:relative;width:1200px;height:2688px;overflow:hidden}

/* hero */
.hero{position:absolute;left:0;top:0;width:1200px;height:560px;
  background:linear-gradient(120deg,var(--navy) 0%,var(--blue) 45%,var(--blue-light) 75%,var(--violet) 100%);overflow:hidden}
.hero::after{content:"";position:absolute;right:-120px;top:-160px;width:560px;height:560px;border-radius:50%;background:rgba(255,255,255,.06)}
.topbar{position:absolute;right:40px;top:14px;display:flex;gap:26px;font-size:12px;color:#dfe5ff;align-items:center}
.topbar span{display:flex;align-items:center;gap:6px}
.topbar svg{width:14px;height:14px}
.brand{position:absolute;left:40px;top:40px;display:flex;align-items:center;gap:10px;color:var(--white);font-weight:700;font-size:17px;letter-spacing:1px}
.brand i{width:26px;height:26px;border-radius:50%;background:var(--orange);display:block}
.nav{position:absolute;left:380px;top:58px;display:flex;gap:34px;font-size:13px;color:#e6ebff}
.nav a{color:inherit;text-decoration:none}
.nav a.active{color:var(--white);font-weight:600;border-bottom:2px solid var(--orange);padding-bottom:4px}
.socials{position:absolute;right:40px;top:58px;display:flex;gap:12px}
.socials i{display:block;width:18px;height:18px;border-radius:50%;background:rgba(255,255,255,.75)}

.hero-copy{position:absolute;left:80px;top:220px;width:580px;z-index:1}
.slide-no{color:var(--white);font-size:28px;font-weight:600;margin-bottom:10px}
.slide-no small{font-size:12px;opacity:.7;margin-left:6px}
.hero h1{font-size:32px;line-height:1.25;color:#ffd95c;font-weight:700;margin-bottom:14px}
.hero h1 span{color:var(--white);font-weight:500}
.hero p.lead{width:420px;font-size:12px;line-height:1.6;color:#d7defc;margin-bottom:16px}
.read-more{color:var(--white);font-size:12px;font-weight:600;display:flex;gap:8px;align-items:center}

.callback{position:absolute;left:770px;top:120px;width:390px;height:370px;background:rgba(39,56,160,.85);border-radius:6px;padding:26px 30px;box-shadow:0 10px 30px rgba(0,0,0,.2);z-index:1}
.callback h3{color:var(--white);text-align:center;font-size:18px;line-height:1.3;font-weight:600;margin-bottom:18px}
.field{display:flex;align-items:center;gap:10px;margin-bottom:12px;color:var(--white);font-size:12px}
.field label{width:56px;white-space:nowrap}
.field div{flex:1;height:30px;background:var(--white);border-radius:3px}
.field.tall div{height:70px}
.callback .btn{display:block;margin:8px auto 0 66px;width:96px;height:28px;border-radius:3px;background:var(--blue-light);color:var(--white);font-size:11px;text-align:center;line-height:28px}

/* service strip */
.services{position:absolute;left:0;top:560px;width:1200px;height:72px;display:flex}
.services div{flex:1;display:flex;align-items:center;gap:10px;padding-left:22px;color:var(--white);font-size:13px;font-weight:600;white-space:nowrap}
.services svg{width:20px;height:20px;flex:none}
.s1{background:var(--orange)}.s2{background:var(--coral)}.s3{background:var(--sky)}.s4{background:var(--teal)}

/* who we are */
.ghost{position:absolute;left:0;width:1200px;text-align:center;font-size:72px;font-weight:800;color:#eef0f6;letter-spacing:2px}
.section-title{position:absolute;left:0;width:1200px;text-align:center;font-size:32px;font-weight:700;color:var(--ink)}
.who-intro{position:absolute;left:350px;top:760px;width:500px;text-align:center;font-size:10px;line-height:1.6}
.who-body{position:absolute;left:160px;top:820px;width:880px;text-align:center;font-size:11px;line-height:1.7}

.ring{position:absolute;left:880px;top:860px;width:620px;height:620px;border-radius:50%;border:80px solid var(--ring);opacity:.8}
.dot{position:absolute;border-radius:50%}

/* what we do */
.what{position:absolute;left:160px;top:950px;width:500px}
.what .kicker{font-size:10px;color:var(--ink);margin-bottom:10px}
.what .tag{font-size:11px;color:var(--ink);margin-bottom:10px}
.what h2{font-size:28px;color:var(--ink);font-weight:700;margin-bottom:14px}
.what p{font-size:11px;line-height:1.7;margin-bottom:12px}
.what .more{font-size:12px;color:var(--ink);font-weight:600}
.what-photo{position:absolute;left:820px;top:1030px;width:340px;height:170px;background:linear-gradient(135deg,#7b8aa8,#c9b7a2 55%,#4d5b78);border-radius:2px}

/* team */
.team{position:absolute;left:230px;top:1580px;display:flex;gap:22px}
.card{width:170px;height:170px;background:var(--white);box-shadow:0 4px 16px rgba(30,40,90,.1);border-radius:4px;text-align:center;padding-top:10px}
.avatar{width:70px;height:70px;border-radius:50%;margin:-44px auto 10px;background:linear-gradient(160deg,#9aa6bb,#4e5a70);border:4px solid var(--white)}
.card h4{font-size:12px;color:var(--ink);font-weight:600;margin-bottom:6px}
.card p{font-size:10px;line-height:1.4;padding:0 14px;margin-bottom:8px}
.card span{display:inline-block;background:var(--navy);color:var(--white);font-size:9px;padding:3px 12px;border-radius:10px}

/* contact */
.contact-bg{position:absolute;left:0;top:1870px;width:1200px;height:640px;background:linear-gradient(180deg,#f5f8fd,var(--white))}
.contact-head{position:absolute;left:160px;top:1872px;width:220px;height:160px;background:var(--navy);padding:30px 24px;color:var(--white)}
.contact-head h2{font-size:24px;font-weight:700;margin-bottom:6px}
.contact-head p{font-size:10px;opacity:.8}
.contact-box{position:absolute;left:160px;top:1990px;width:380px;height:510px;background:var(--pale-blue);padding:24px 22px;color:var(--ink)}
.contact-box h3{font-size:16px;font-weight:600;margin-bottom:12px}
.contact-box p{font-size:11px;line-height:1.6;margin-bottom:10px}
.contact-box b{font-weight:600}
.input{height:34px;background:var(--white);border-radius:3px;margin:10px 0 0 40px;width:260px;font-size:10px;color:#9aa0b0;padding:10px 14px}
.input.tall{height:60px}
.contact-box .more{margin-top:22px;font-size:12px;font-weight:600}
.map{position:absolute;left:540px;top:1872px;width:620px;height:628px;background:linear-gradient(135deg,#e7e9ec,#d3d7dc 60%,#e2e4e7)}

/* footer */
.footer{position:absolute;left:0;top:2560px;width:1200px;height:128px;background:var(--footer);color:#c9cad0;text-align:center;padding-top:16px}
.footer .fbrand{display:inline-flex;align-items:center;gap:8px;color:var(--white);font-weight:700;font-size:15px;letter-spacing:1px}
.footer .fbrand i{width:20px;height:20px;border-radius:50%;background:var(--orange);display:block}
.footer nav{margin-top:12px;display:flex;justify-content:center;gap:30px;font-size:11px}
.footer .fsoc{margin-top:10px;display:flex;justify-content:center;gap:12px}
.footer .fsoc i{width:16px;height:16px;border-radius:50%;background:#8d8f96;display:block}
.footer small{display:block;margin-top:10px;font-size:10px;color:#8d8f96}
</style>
</head>
<body>
<div class="page">

  <header class="hero">
    <div class="topbar">
      <span><svg viewBox="0 0 24 24" fill="#fff"><path d="M6.6 10.8a15 15 0 006.6 6.6l2.2-2.2a1 1 0 011-.25 11.4 11.4 0 003.6.6 1 1 0 011 1V20a1 1 0 01-1 1A17 17 0 013 4a1 1 0 011-1h3.5a1 1 0 011 1 11.4 11.4 0 00.6 3.6 1 1 0 01-.25 1z"/></svg>+244 900 000 111</span>
      <span><svg viewBox="0 0 24 24" fill="none"><path d="M3 5h18v14H3z" stroke="#fff" stroke-width="2"/><path d="M3 5l9 7 9-7" stroke="#fff" stroke-width="2"/></svg>hello@zephylbrokers.ao</span>
    </div>
    <div class="brand"><i></i>ZEPHYL BROKERS</div>
    <nav class="nav">
      <a class="active">Home</a><a>Who we are</a><a>Our Team</a><a>What we do</a><a>Contact Us</a>
    </nav>
    <div class="socials"><i></i><i></i><i></i></div>

    <div class="hero-copy">
      <div class="slide-no">01<small>Banner 04</small></div>
      <h1>Lorem Ipsum is simply dummy typesetting industry <span>Time and Time Again</span></h1>
      <p class="lead">Lorem Ipsum is simply dummy text of the printing and typesetting industry. Lorem Ipsum has been the industry's standard text.</p>
      <div class="read-more">Read More
        <svg width="16" height="10" viewBox="0 0 16 10"><path d="M0 5h14M10 1l4 4-4 4" stroke="#fff" stroke-width="1.6" fill="none"/></svg></div>
    </div>

    <form class="callback">
      <h3>Fill Up The Form To<br>Get A Quick Call Back From Us!</h3>
      <div class="field"><label>Name *</label><div></div></div>
      <div class="field"><label>Email *</label><div></div></div>
      <div class="field"><label>Phone *</label><div></div></div>
      <div class="field tall"><label>Query *</label><div></div></div>
      <span class="btn">Submit Query</span>
    </form>
  </header>

  <section class="services">
    <div class="s1"><svg viewBox="0 0 24 24" fill="none" stroke="#fff" stroke-width="2"><rect x="3" y="7" width="18" height="13"/><path d="M8 7V4h8v3"/></svg>Bulk</div>
    <div class="s2"><svg viewBox="0 0 24 24" fill="none" stroke="#fff" stroke-width="2"><path d="M12 3c4 6 6 9 6 12a6 6 0 01-12 0c0-3 2-6 6-12z"/></svg>Oil and gas companies</div>
    <div class="s3"><svg viewBox="0 0 24 24" fill="none" stroke="#fff" stroke-width="2"><path d="M4 5h16v11H9l-5 4z"/></svg>French speaking copying</div>
    <div class="s4"><svg viewBox="0 0 24 24" fill="none" stroke="#fff" stroke-width="2"><path d="M3 20V10l6 4V10l6 4V6h6v14z"/></svg>Factories and importers of goods</div>
  </section>

  <div class="ring"></div>
  <div class="dot" style="left:880px;top:740px;width:22px;height:22px;background:#c7c0f0"></div>
  <div class="dot" style="left:100px;top:1080px;width:18px;height:18px;background:#8a7fe0"></div>
  <div class="dot" style="left:1130px;top:1500px;width:14px;height:14px;background:#8fb3f0"></div>

  <section>
    <div class="ghost" style="top:660px">What We are</div>
    <h2 class="section-title" style="top:694px">What We are</h2>
    <p class="who-intro">Lorem Ipsum is simply dummy text of the printing and typesetting industry. Lorem Ipsum has been the standard.</p>
    <p class="who-body">Lorem Ipsum is simply dummy text of the printing and typesetting industry. Lorem Ipsum has been the industry's standard dummy text ever since the 1500s, when an unknown printer took a galley of type and scrambled it to make a type specimen book. It has survived not only five centuries, but also the leap into electronic typesetting, remaining essentially unchanged. It was popularised in the 1960s with the release of sheets containing passages, and more recently with desktop publishing software like page makers including versions of Lorem Ipsum.</p>
  </section>

  <section class="what">
    <div class="kicker">— Lorem Ipsum is simply</div>
    <div class="tag">Lorem Ipsum is simply dummy text of the printing and typesetting industry. Lorem Ipsum has been standard.</div>
    <h2>what we do</h2>
    <p>Lorem Ipsum is simply dummy text of the printing and typesetting industry. Lorem Ipsum has been the industry's standard dummy text ever since the 1500s, when an unknown printer took a galley of type and scrambled it to make a type specimen book.</p>
    <p>It has survived not only five centuries, but also the leap into electronic typesetting, remaining essentially unchanged. It was popularised in the 1960s with the release of sheets containing passages, and more recently with desktop publishing software like page makers including versions of Lorem Ipsum. Contrary to popular belief, it is not simply random text.</p>
    <div class="more">Read More →</div>
  </section>
  <div class="what-photo" role="img" aria-label="Photo of a business team meeting around a table with laptops"></div>

  <section>
    <div class="ghost" style="top:1380px">Team</div>
    <h2 class="section-title" style="top:1420px">Our Team</h2>
    <div class="team">
      <div class="card"><div class="avatar" role="img" aria-label="Portrait photo of a team member"></div><h4>Lorem Ipsum simply</h4><p>It is a long established fact that a reader will be distracted by readable English</p><span>View More</span></div>
      <div class="card"><div class="avatar" role="img" aria-label="Portrait photo of a team member"></div><h4>Lorem Ipsum simply</h4><p>It is a long established fact that a reader will be distracted by readable English</p><span>View More</span></div>
      <div class="card"><div class="avatar" role="img" aria-label="Portrait photo of a team member"></div><h4>Lorem Ipsum simply</h4><p>It is a long established fact that a reader will be distracted by readable English</p><span>View More</span></div>
      <div class="card"><div class="avatar" role="img" aria-label="Portrait photo of a team member"></div><h4>Lorem Ipsum simply</h4><p>It is a long established fact that a reader will be distracted by readable English</p><span>View More</span></div>
    </div>
  </section>

  <div class="contact-bg"></div>
  <section>
    <div class="map" role="img" aria-label="Street map of Luanda, Angola showing the office location"></div>
    <div class="contact-head"><h2>Contact Us</h2><p>Get A Quick Call Back</p></div>
    <div class="contact-box">
      <h3>Contact Information</h3>
      <p><b>Address :</b> Lorem Ipsum is simply dummy text of the printing and typesetting industry.</p>
      <p><b>Phone No :</b> +244 900 000 111<br><b>E-mail :</b> hello@zephylbrokers.ao</p>
      <div class="input">Full Name*</div>
      <div class="input">Email Address*</div>
      <div class="input">Contact No*</div>
      <div class="input tall">Message Here*</div>
      <div class="more">Read More →</div>
    </div>
  </section>

  <footer class="footer">
    <div class="fbrand"><i></i>ZEPHYL BROKERS</div>
    <nav><span>Home</span><span>Who we are</span><span>Our Team</span><span>What We do</span><span>Contact Us</span></nav>
    <div class="fsoc"><i></i><i></i><i></i></div>
    <small>© Copyright 2018 Zephyl-Brokers · All Rights Reserved · Terms &amp; Conditions · Privacy Policy</small>
  </footer>

</div>
</body>
</html>
```